Vinyl Sign for Sports Bar

Need sign 109" x 61". 2 colors. Black and another PMS color. The name of the bar is Crestview. It is a Bar and Grill. It will be a sports theme.

Industry/Entity Type

Sports Bar

Requirements
Must have
• Must have good readability from the street while driving by. Must be a Vector PDF file to give to the vinyl sign cutter.

```html
<!DOCTYPE html>
<html lang="en">
<head>
<meta charset="utf-8">
<title>Crestview Bar &amp; Grill – Vinyl Sign Concepts</title>
<link rel="stylesheet" href="https://fonts.googleapis.com/css2?family=Montserrat:wght@700&display=swap">
<style>
  :root {
    --sign-black: #000000;
    --sign-gold: #ffcc00;
    --page: #ffffff;
  }
  html, body {
    margin: 0;
    padding: 0;
    width: 1200px;
    height: 848px;
    overflow: hidden;
    background: var(--page);
  }
  .canvas {
    position: relative;
    width: 1200px;
    height: 848px;
  }
  .sign {
    position: absolute;
    width: 803px;
    height: 290px;
    display: block;
  }
  .sign--dark  { left: 200px; top: 102px; --field: var(--sign-black); --ink: var(--sign-gold); }
  .sign--light { left: 197px; top: 454px; --field: var(--sign-gold); --ink: var(--sign-black); }

  .sign__field  { fill: var(--field); }
  .sign__stripe { fill: var(--ink); }
  .sign__est, .sign__name, .sign__tagline {
    fill: var(--ink);
    font-family: "Montserrat", Arial, sans-serif;
    font-weight: 700;
  }
  .sign__est     { font-size: 26px; }
  .sign__name    { font-size: 64px; }
  .sign__tagline { font-size: 30px; }
</style>
</head>
<body>
<main class="canvas">

  <svg class="sign sign--dark" viewBox="0 0 803 290" aria-labelledby="sign-dark-title">
    <title id="sign-dark-title">Crestview Bar &amp; Grill, established 2013 – gold on black</title>
    <rect class="sign__field" width="803" height="290"/>
    <polygon class="sign__stripe" points="160,0 180,0 0,180 0,160"/>
    <polygon class="sign__stripe" points="198,0 218,0 0,218 0,198"/>
    <polygon class="sign__stripe" points="803,102 803,122 635,290 615,290"/>
    <polygon class="sign__stripe" points="803,142 803,162 675,290 655,290"/>
    <text class="sign__est" x="403" y="76" text-anchor="middle" textLength="150" lengthAdjust="spacingAndGlyphs">EST. 2013</text>
    <text class="sign__name" x="403" y="160" text-anchor="middle" textLength="338" lengthAdjust="spacingAndGlyphs">CRESTVIEW</text>
    <text class="sign__tagline" x="403" y="216" text-anchor="middle" textLength="220" lengthAdjust="spacingAndGlyphs">BAR &amp; GRILL</text>
  </svg>

  <svg class="sign sign--light" viewBox="0 0 803 290" aria-labelledby="sign-light-title">
    <title id="sign-light-title">Crestview Bar &amp; Grill, established 2013 – black on gold</title>
    <rect class="sign__field" width="803" height="290"/>
    <polygon class="sign__stripe" points="130,0 150,0 0,150 0,130"/>
    <polygon class="sign__stripe" points="168,0 188,0 0,188 0,168"/>
    <polygon class="sign__stripe" points="803,102 803,122 635,290 615,290"/>
    <polygon class="sign__stripe" points="803,142 803,162 675,290 655,290"/>
    <text class="sign__est" x="403" y="76" text-anchor="middle" textLength="150" lengthAdjust="spacingAndGlyphs">EST. 2013</text>
    <text class="sign__name" x="403" y="160" text-anchor="middle" textLength="338" lengthAdjust="spacingAndGlyphs">CRESTVIEW</text>
    <text class="sign__tagline" x="403" y="216" text-anchor="middle" textLength="220" lengthAdjust="spacingAndGlyphs">BAR &amp; GRILL</text>
  </svg>

</main>
</body>
</html>
```